BRL Design Business Card

I need to develop a business card for my real estate design and investment company. Something clean, classic and professional with a modern vibe.

Industry/Entity Type

Real Estate

Font styles to use
Serif
Sans Serif

```html
<!DOCTYPE html>
<html lang="en">
<head>
<meta charset="utf-8">
<title>BRL Design Business Card</title>
<link rel="stylesheet" href="https://fonts.googleapis.com/css2?family=Josefin+Sans:wght@300&family=Open+Sans:wght@400;600;800&display=swap">
<style>
  :root {
    --backdrop: #e9e4e1;
    --cocoa: #2a1a1d;
    --blush: #fbe8ea;
    --ink-light: #f6eef0;
  }
  * { margin: 0; padding: 0; box-sizing: border-box; }
  html, body { width: 1200px; height: 903px; overflow: hidden; }
  body {
    background: var(--backdrop);
    font-family: "Open Sans", Arial, sans-serif;
    position: relative;
  }
  .card {
    position: absolute;
    top: 296px;
    width: 540px;
    height: 310px;
    border-radius: 18px;
    background: var(--cocoa);
    overflow: hidden;
    box-shadow: 0 6px 18px rgba(0,0,0,0.18);
  }
  .card-front { left: 45px; }
  .card-back { left: 615px; }

  .brand {
    font-family: "Josefin Sans", Arial, sans-serif;
    font-weight: 300;
    text-align: center;
    position: absolute;
  }
  .brand-mark { font-size: 84px; letter-spacing: 10px; line-height: 1; }
  .brand-line { font-size: 22px; letter-spacing: 0.5px; margin-top: 4px; }

  .card-front .brand {
    color: var(--ink-light);
    left: 0; right: 0; top: 78px;
  }
  .front-web {
    position: absolute;
    left: 0; right: 0; bottom: 40px;
    text-align: center;
    color: var(--ink-light);
    font-size: 15px;
    letter-spacing: 0.5px;
  }

  .back-shape { position: absolute; inset: 0; }
  .card-back .brand {
    color: var(--cocoa);
    left: 0; width: 235px; top: 100px;
  }
  .card-back .brand-mark { font-size: 62px; letter-spacing: 6px; }
  .card-back .brand-line { font-size: 15px; }

  .contact {
    position: absolute;
    left: 290px; right: 24px; top: 40px;
    color: var(--ink-light);
    text-align: center;
  }
  .contact-name { font-size: 30px; font-weight: 800; letter-spacing: 1px; }
  .contact-role { font-size: 17px; font-weight: 600; margin-bottom: 22px; }
  .contact-line { font-size: 13px; line-height: 1.6; }
  .contact-gap { height: 10px; }
</style>
</head>
<body>
  <section class="card card-front">
    <div class="brand">
      <div class="brand-mark">BRL</div>
      <div class="brand-line">Design and Productions</div>
    </div>
    <p class="front-web">yourwebsitebrl.com</p>
  </section>

  <section class="card card-back">
    <svg class="back-shape" width="540" height="310" viewBox="0 0 540 310" aria-hidden="true">
      <circle cx="-40" cy="155" r="270" fill="var(--blush)"/>
      <circle cx="-40" cy="155" r="283" fill="none" stroke="var(--blush)" stroke-width="4"/>
    </svg>
    <div class="brand">
      <div class="brand-mark">BRL</div>
      <div class="brand-line">Design and Productions</div>
    </div>
    <div class="contact">
      <p class="contact-name">Your Name</p>
      <p class="contact-role">Designation</p>
      <p class="contact-line">111,Lorem Ipsum Street,</p>
      <p class="contact-line">Lorem Ipsum LW-123</p>
      <p class="contact-line">123 456 789,987 654 321</p>
      <div class="contact-gap"></div>
      <p class="contact-line">yourmailid@brl.com</p>
      <div class="contact-gap"></div>
      <p class="contact-line">yourwebsitebrl.com</p>
    </div>
  </section>
</body>
</html>
```